Sci-Fi Safari-E-Book Cover

We're looking for a cover for a science fiction novel that will be sold as an E-Book. The theme of the book includes a safari on an alien world, where the main goal is to kill a red lion (which is the same as African lions on this world, only bigger).

The background will be preferably black, with most of the cover taken up (in the middle) by an image of the lion peering straight out from the darkness. Not much will be visible, probably just the glowing eyes, a little bit of the nose, and some of the fangs.

At the very top we'd like the cover to include the series' title: "Under Watch."

And just below that in somewhat larger letters we'd like it to say "The Fenway Baron."

At the bottom we want it to say "Derek Asholt," in smaller letters. We're thinking we want a red font, and perhaps highlighted by some sort of lighting effect. We're not completely decided on that, however.

Thank you for your interest
Updates

Hello, we haven't previously clarified this, but we'd like the ratio for this book cover to 1.6, or near that.

Thank you

Target Market(s)

English science fiction novel readers.

Requirements
Must have
• Text that says (in this order):

Under Watch (at the top of the page)
The Fenway Baron (just below "Under Watch", with slightly larger font)

Derek Asholt (at the bottom of the page)
-
Black background
Lion face peering out of shadows
Lion's eyes with slanted irises
Visible Fangs
-
Image details: 1.6 ratio
Nice to have
• More of a photo-realistic feel to the lion, rather than art-like feel.

Some sort of lighting affect around the text "Under Watch" & "The Fenway Baron."

```html
<!DOCTYPE html>
<html lang="en">
<head>
<meta charset="utf-8">
<title>Under Watch – The Fenway Baron – Cover Wrap</title>
<link href="https://fonts.googleapis.com/css2?family=Stardos+Stencil:wght@700&family=Oswald:wght@600&family=Cinzel:wght@700&family=Cabin:wght@400&display=swap" rel="stylesheet">
<style>
  :root {
    --stage: #e6e6e6;
    --cover-black: #050404;
    --title-red: #d21a1a;
    --title-glow: rgba(255, 40, 30, 0.85);
    --subtitle-pink: #e7c6c4;
    --body-grey: #c9c9c9;
    --placeholder: #d8d8d8;
    --placeholder-text: #1d1d1d;
    --white: #ffffff;
    --mane-light: #e7a54a;
    --mane-mid: #a9561c;
    --mane-dark: #2a1207;
  }
  * { box-sizing: border-box; margin: 0; padding: 0; }
  html, body {
    width: 1200px; height: 800px; overflow: hidden;
    background: var(--stage);
  }
  .wrap {
    position: absolute; left: 170px; top: 85px;
    display: flex; height: 630px;
    box-shadow: 0 14px 30px rgba(0,0,0,0.25);
  }
  .back-cover, .spine, .front-cover {
    position: relative; height: 100%; background: var(--cover-black);
  }
  .back-cover {
    width: 420px; padding: 26px 30px 16px; text-align: center;
    display: flex; flex-direction: column;
  }
  .spine { width: 40px; border-left: 1px solid #1a1a1a; border-right: 1px solid #1a1a1a; }
  .front-cover { width: 420px; overflow: hidden; }

  .series-title {
    font-family: "Stardos Stencil", serif; font-weight: 700;
    color: rgba(120, 10, 10, 0.55);
    -webkit-text-stroke: 1.5px var(--title-red);
    text-shadow: 0 0 6px var(--title-glow), 0 0 14px rgba(255,0,0,0.5);
    letter-spacing: 1px; line-height: 1; white-space: nowrap;
  }
  .back-cover .author-kicker {
    font-family: "Cinzel", serif; font-size: 11px; color: var(--white);
    text-align: right; letter-spacing: 0.5px;
  }
  .back-cover .series-title { font-size: 40px; margin-top: 10px; }
  .back-cover .book-title {
    font-family: "Oswald", sans-serif; font-weight: 600; font-size: 20px;
    letter-spacing: 6px; color: var(--subtitle-pink); margin-top: 14px;
    text-shadow: 0 0 4px rgba(210,30,30,0.7); white-space: nowrap;
  }
  .blurb {
    font-family: "Cabin", sans-serif; font-size: 11.3px; line-height: 1.36;
    color: var(--body-grey); margin-top: 22px;
  }
  .back-footer {
    margin-top: auto;
    display: flex; justify-content: space-between;
  }
  .placeholder-box {
    width: 106px; height: 52px; background: var(--placeholder);
    display: flex; align-items: center; justify-content: center;
    font-family: "Cabin", sans-serif; font-weight: 400; font-size: 13px;
    color: var(--placeholder-text); letter-spacing: 0.5px;
  }
  .copyright {
    margin-top: 18px;
    font-family: "Cinzel", serif; font-size: 7px; color: var(--body-grey);
    letter-spacing: 0.5px;
  }

  .spine-title, .spine-author {
    position: absolute; left: 50%; white-space: nowrap;
    transform: translateX(-50%) rotate(90deg); transform-origin: center;
  }
  .spine-title { top: 150px; font-size: 24px; letter-spacing: 3px; }
  .spine-author {
    top: 470px; font-family: "Cinzel", serif; font-size: 10px;
    color: var(--white); letter-spacing: 1px;
  }

  .lion-art {
    position: absolute; left: 0; top: 90px; width: 420px; height: 480px;
  }
  .front-cover .series-title {
    position: absolute; top: 28px; left: 0; right: 0; text-align: center;
    font-size: 46px; letter-spacing: 2px;
  }
  .front-cover .book-title {
    position: absolute; top: 508px; left: 0; right: 0; text-align: center;
    font-family: "Oswald", sans-serif; font-weight: 600; font-size: 40px;
    color: var(--white); letter-spacing: 0.5px; white-space: nowrap;
    -webkit-text-stroke: 1px var(--title-red);
    text-shadow: 0 0 4px rgba(200,20,20,0.9);
  }
  .front-cover .author-name {
    position: absolute; top: 580px; left: 0; right: 0; text-align: center;
    font-family: "Cinzel", serif; font-weight: 700; font-size: 16px;
    color: var(--white); letter-spacing: 0.5px;
  }
</style>
</head>
<body>
  <div class="wrap">
    <section class="back-cover">
      <p class="author-kicker">DEREK ASHOLT'S</p>
      <h2 class="series-title">UNDER WATCH</h2>
      <p class="book-title">THE FENWAY BARON</p>
      <p class="blurb">Lorem ipsum dolor sit amet, consectetur adipisicing elit, sed do eiusmod tempor incididunt ut labore et dolore magna aliqua. Ut enim ad minim veniam, quis nostrud exercitation. Lorem ipsum dolor sit amet, consectetur adipisicing elit, sed do eiusmod tempor incididunt ut labore et dolore magna aliqua. Ut enim ad minim veniam, quis nostrud exercitation. Lorem ipsum dolor sit amet, consectetur adipisicing elit, sed do eiusmod tempor incididunt ut labore et dolore magna aliqua. Ut enim ad minim veniam, quis nostrud exercitation. Lorem ipsum dolor sit amet, consectetur adipisicing elit, sed do eiusmod tempor incididunt ut labore et dolore magna aliqua. Ut enim ad minim veniam, quis nostrud exercitation. Lorem ipsum dolor sit amet, consectetur adipisicing elit.</p>
      <div class="back-footer">
        <div class="placeholder-box">LOGO</div>
        <div class="placeholder-box">ISBN</div>
      </div>
      <p class="copyright">COPYRIGHT © 2012 BY DEREK ASHOLT</p>
    </section>

    <section class="spine">
      <p class="series-title spine-title">UNDER WATCH</p>
      <p class="spine-author">DEREK ASHOLT</p>
    </section>

    <section class="front-cover">
      <svg class="lion-art" viewBox="0 0 420 480" role="img" aria-label="Photograph of a lion's face with red eyes staring straight out from the darkness, golden mane fading into black">
        <defs>
          <radialGradient id="mane-glow" cx="50%" cy="45%" r="55%">
            <stop offset="0%" stop-color="var(--mane-light)"/>
            <stop offset="45%" stop-color="var(--mane-mid)"/>
            <stop offset="80%" stop-color="var(--mane-dark)"/>
            <stop offset="100%" stop-color="var(--cover-black)"/>
          </radialGradient>
        </defs>
        <rect width="420" height="480" fill="url(#mane-glow)"/>
      </svg>
      <h1 class="series-title">UNDER WATCH</h1>
      <p class="book-title">THE FENWAY BARON</p>
      <p class="author-name">DEREK ASHOLT</p>
    </section>
  </div>
</body>
</html>
```